Veterinary Hospital Business Card

We have recently updated our logo and wish to have a business card designed incorporating the new look and flow. We are a full service veterinary hospital also offering laser therapy, boarding, and grooming. Our website is www.marlowpaws.com

Industry/Entity Type

Veterinary

```html
<!DOCTYPE html>
<html lang="en">
<head>
<meta charset="utf-8">
<title>Marlow Animal Hospital – Business Card</title>
<link rel="stylesheet" href="https://fonts.googleapis.com/css2?family=Ubuntu:wght@400;500&display=swap">
<style>
  :root {
    --navy: #173f63;
    --steel: #41708a;
    --sky: #7ea6bd;
    --paper: #ffffff;
  }
  html, body {
    margin: 0;
    padding: 0;
    width: 1200px;
    height: 1200px;
    overflow: hidden;
    background: var(--paper);
  }
  .canvas {
    position: relative;
    width: 1200px;
    height: 1200px;
    font-family: "Ubuntu", sans-serif;
    color: var(--navy);
  }
  .card {
    position: absolute;
    top: 251px;
    width: 503px;
    height: 681px;
    box-sizing: border-box;
    border: 3px solid var(--steel);
    background: var(--paper);
  }
  .card--front { left: 76px; }
  .card--back  { left: 637px; }

  /* Front: wordmark */
  .wordmark {
    position: absolute;
    left: 0;
    right: 0;
    top: 200px;
    margin: 0;
    text-align: center;
    font-family: "Ubuntu", sans-serif;
    font-weight: 500;
    font-size: 68px;
    line-height: 1.05;
    letter-spacing: 1px;
    text-transform: uppercase;
    color: var(--navy);
  }
  .wordmark span { display: block; }

  /* Back */
  .cat-art {
    position: absolute;
    left: 85px;
    top: 54px;
    width: 123px;
    height: 93px;
    border-radius: 40px 40px 6px 6px;
    background: linear-gradient(180deg, var(--steel), #4f7e97);
  }
  .services {
    position: absolute;
    left: 0;
    right: 0;
    top: 160px;
    margin: 0;
    padding: 0;
    list-style: none;
    text-align: center;
  }
  .service {
    font-size: 39px;
    line-height: 46px;
    color: var(--navy);
  }
  .service-dot {
    display: block;
    width: 16px;
    height: 16px;
    margin: 26px auto 26px;
    border-radius: 50%;
    background: var(--sky);
  }
  .contact {
    position: absolute;
    left: 0;
    right: 0;
    top: 440px;
    margin: 0;
    text-align: center;
    font-style: normal;
    font-size: 25px;
    line-height: 39.5px;
    color: var(--navy);
  }
  .contact span { display: block; }
</style>
</head>
<body>
<main class="canvas">
  <section class="card card--front" aria-label="Card front">
    <h1 class="wordmark">
      <span>Marlow</span>
      <span>Animal</span>
      <span>Hospital</span>
    </h1>
  </section>

  <section class="card card--back" aria-label="Card back">
    <div class="cat-art" role="img" aria-label="Silhouette of a sitting cat"></div>
    <ul class="services">
      <li class="service">laser therapy</li>
      <li class="service-dot" aria-hidden="true"></li>
      <li class="service">boarding</li>
      <li class="service-dot" aria-hidden="true"></li>
      <li class="service">grooming</li>
    </ul>
    <address class="contact">
      <span>1180 Marlow Rd</span>
      <span>Fairview, SC</span>
      <span>29640</span>
      <span>Ph: (803) 555-0142</span>
      <span>clientcare@marlowpaws.com</span>
    </address>
  </section>
</main>
</body>
</html>
```